Social News web page design website name Velnu.

I need a web design for a start up project called Velnu based in Sydney. Its a social news website. it helps people to get centralized news and people can have their own profiles where they can post there thoughts and comments and it will be free to signup and usage as well.

I would like to see designs that use the latest murlan bootstrap framework and are mobile compatible. only need 2 pages a home page kind of similar to
plom (http://plom.example/) and a profile that's a next gen user profile page I will leave that to you imaginations

this is my previous design I did on my own http://www.velnu-site.example/

Target Market(s)

target market is 13 and up and anyone who likes or uses social media and would be able to understand the site

Industry/Entity Type

News

Requirements
Must have
• 1.) using murlan bootstrap. 2) a home page similar to plom (http://plom.example/) or even better free to use your imagination 3) a next gen profile page better the one i made on my own which is this one (http://www.velnu-site.example/profile/korelatimbo) 4) for mobile navigation, have a mobile navigation something similar to http://zanpel.wovrite.example/
Nice to have
• 1) a sexy navigation and layout for both desktop and mobile phones. i will leave that to you imaginations. 2) social medial buttons like to sign-in with and also to post a story to Linkora or murlan 3) a user settings page (but not necessary) 4) a login or signup (but not necessary)

```html
<!DOCTYPE html>
<html lang="en">
<head>
<meta charset="utf-8">
<title>Velnu — Social News</title>
<link href="https://fonts.googleapis.com/css2?family=Open+Sans:wght@400;600;700&display=swap" rel="stylesheet">
<style>
:root{
  --page-bg:#e9e9e9;
  --panel:#ffffff;
  --dark:#2b2b2b;
  --darker:#222222;
  --text:#333333;
  --muted:#8a8a8a;
  --link:#3a9ad9;
  --btn:#2f8fe0;
  --btn-dark:#3a3a3a;
  --line:#dcdcdc;
}
*{box-sizing:border-box;margin:0;padding:0}
html,body{width:863px;height:1200px;overflow:hidden}
body{background:var(--page-bg);font-family:'Open Sans',sans-serif;color:var(--text);position:relative}
.topbar{position:absolute;left:0;top:0;width:863px;height:37px;background:linear-gradient(#ffffff,#f1f1f1);border-bottom:1px solid #d0d0d0}
.brand{position:absolute;left:178px;top:9px;font-size:14px;font-weight:700;color:#222}
.brand-sep{position:absolute;left:228px;top:11px;width:1px;height:17px;background:#ccc}
.nav-home{position:absolute;left:237px;top:15px;font-size:7px;color:#555}
.auth{position:absolute;top:11px;display:flex;gap:5px;left:584px}
.auth a{display:block;width:48px;height:16px;line-height:16px;text-align:center;background:var(--btn-dark);color:#fff;font-size:6.5px;font-weight:700;text-decoration:none;border:1px solid #111}
.filterbar{position:absolute;left:0;top:37px;width:863px;height:28px;background:var(--dark)}
.select{position:absolute;top:6px;height:17px;background:#1e1e1e;border:1px solid #3a3a3a;color:#666;font-size:6.5px;line-height:15px;padding-left:5px}
.select::after{content:"▾";position:absolute;right:5px;color:#aaa}
.cat{left:178px;width:118px}
.lang{left:616px;width:68px}
.county-label{position:absolute;left:521px;top:14px;font-size:6.5px;color:#999}
.panel{position:absolute;left:173px;top:66px;width:517px;height:1040px;background:var(--panel)}
.hero{position:absolute;left:180px;top:84px;width:502px;height:185px;border:2px solid #cfcfcf;background:linear-gradient(100deg,#3c3f44 0%,#6b6f75 30%,#1f2b45 55%,#9a1d2a 60%,#2a3450 66%,#b9aba0 85%,#53575c 100%)}
.hero-caption{position:absolute;left:8px;top:66px;width:228px;height:112px;background:rgba(25,25,25,.82);padding:10px 8px;color:#fff}
.hero-caption h2{font-size:11.5px;font-weight:600;margin-bottom:4px}
.hero-caption p{font-size:6.5px;line-height:13px;color:#ddd}
.dots{position:absolute;left:11px;top:166px;display:flex;gap:2px}
.dots span{width:6px;height:6px;border-radius:50%;background:#fff}
.dots span:first-child{background:#888}
.sortbar{position:absolute;left:178px;top:290px;width:510px;height:29px;border:1px solid var(--line);background:linear-gradient(#fafafa,#efefef);font-size:6.5px;font-weight:600}
.sortbar .opt{position:absolute;top:12px}
.sortbar .divider{position:absolute;top:6px;width:1px;height:18px;background:#ddd}
.pager{position:absolute;left:446px;top:8px;display:flex;align-items:center;gap:4px}
.pager i{display:block;width:13px;height:12px;background:#444}
.section-title{position:absolute;left:178px;top:342px;font-size:8.5px;font-weight:700}
.grid{position:absolute;left:177px;top:358px;width:510px;display:grid;grid-template-columns:repeat(3,163px);grid-template-rows:252px 260px 240px;column-gap:10px}
.card{position:relative}
.thumb{width:163px;height:110px;border:1px solid #ddd}
.card h3{margin-top:18px;font-size:7.5px;font-weight:600;line-height:14px}
.card .src{font-size:6.5px;color:var(--link);line-height:12px}
.card p{font-size:5.3px;color:var(--muted);line-height:11px;margin-top:1px}
.card .actions{position:absolute;left:0;top:203px;width:163px;display:flex;justify-content:space-between;align-items:center}
.share{display:flex;align-items:center;gap:2px;width:62px;height:18px;background:var(--btn);border:1px solid #1e6fb5;color:#fff;font-size:6px;padding-left:3px}
.vote{font-size:6.5px;font-weight:600;color:#444}
.footer{position:absolute;left:0;top:1158px;width:863px;height:42px;background:var(--darker);color:#ccc;font-size:8.5px}
.footer .links{position:absolute;left:176px;top:16px}
.footer .copy{position:absolute;left:543px;top:16px}
</style>
</head>
<body>
<header class="topbar">
  <div class="brand">Velnu</div>
  <div class="brand-sep"></div>
  <div class="nav-home">Home</div>
  <nav class="auth"><a href="#">SIGN IN</a><a href="#">SIGN UP</a></nav>
</header>
<div class="filterbar">
  <div class="select cat">Select Category</div>
  <div class="county-label">Choose Your Prefered County</div>
  <div class="select lang">English</div>
</div>
<main class="panel"></main>
<section class="hero" role="img" aria-label="Photo of reporters holding microphones toward a man in a suit and red tie">
  <div class="hero-caption">
    <h2>Neque porro quisquam est qui</h2>
    <p>Dolorem ipsum quia dolor sit amet, consectetur, adipisci velit Lorem ipsum dolor sit amet, consectetur adipisicing elit, sed do eiusmod tempor incididunt ut labore et dolore magna aliqua.</p>
  </div>
  <div class="dots"><span></span><span></span><span></span><span></span></div>
</section>
<div class="sortbar">
  <span class="opt" style="left:10px">SORT BY ▸</span>
  <span class="divider" style="left:56px"></span>
  <span class="opt" style="left:61px">STORIES</span>
  <span class="divider" style="left:101px"></span>
  <span class="opt" style="left:108px">POPULAR</span>
  <span class="divider" style="left:151px"></span>
  <span class="opt" style="left:158px">NEWEST</span>
  <div class="pager"><span style="margin-right:2px">PAGES</span>
    <svg width="13" height="12"><rect width="13" height="12" fill="#444"/><path d="M8 3 L4 6 L8 9Z" fill="#fff"/></svg>
    <svg width="13" height="12" style="margin-left:6px"><rect width="13" height="12" fill="#444"/><path d="M5 3 L9 6 L5 9Z" fill="#fff"/></svg>
  </div>
</div>
<div class="section-title">STORIES</div>
<div class="grid">
  <article class="card"><div class="thumb" role="img" aria-label="Injured football player on the sideline" style="background:linear-gradient(135deg,#3b4f8a,#b8343c 50%,#c9b25a)"></div>
    <h3>Darrel Okonte Injury: Updates on Harbor Kings LB's Leg and Return</h3><div class="src">sportsdesk.example</div>
    <p>Bayview Harbor Kings linebacker Darrel Okonte suffered a scary injury in the League Championship Game against the Northport Gulls</p>
    <div class="actions"><span class="share"><svg width="9" height="8"><path d="M1 7 Q2 3 6 3 V1 L9 4 L6 7 V5 Q3 5 1 7Z" fill="#fff"/></svg>SHARE STORY▾</span><span class="vote">Vote Now (0)</span></div></article>
  <article class="card"><div class="thumb" role="img" aria-label="Portrait of an older man wearing glasses" style="background:linear-gradient(#e2d6ce,#c8aa96)"></div>
    <h3>Darrel Okonte Injury: Updates on Harbor Kings LB's Leg and Return</h3><div class="src">sportsdesk.example</div>
    <p>Bayview Harbor Kings linebacker Darrel Okonte suffered a scary injury in the League Championship Game against the Northport Gulls</p>
    <div class="actions"><span class="share"><svg width="9" height="8"><path d="M1 7 Q2 3 6 3 V1 L9 4 L6 7 V5 Q3 5 1 7Z" fill="#fff"/></svg>SHARE STORY▾</span><span class="vote">Vote Now (0)</span></div></article>
  <article class="card"><div class="thumb" role="img" aria-label="Coach in a cap with a headset" style="background:linear-gradient(135deg,#2a3656,#b88a70 55%,#8a7a66)"></div>
    <h3>Darrel Okonte Injury: Updates on Harbor Kings LB's Leg and Return</h3><div class="src">sportsdesk.example</div>
    <p>Bayview Harbor Kings linebacker Darrel Okonte suffered a scary injury in the League Championship Game against the Northport Gulls</p>
    <div class="actions"><span class="share"><svg width="9" height="8"><path d="M1 7 Q2 3 6 3 V1 L9 4 L6 7 V5 Q3 5 1 7Z" fill="#fff"/></svg>SHARE STORY▾</span><span class="vote">Vote Now (0)</span></div></article>
  <article class="card"><div class="thumb" role="img" aria-label="Graduates in caps and gowns" style="background:linear-gradient(135deg,#cfd4d8,#d86a3a 45%,#1d1d22)"></div>
    <h3>Darrel Okonte Injury: Updates on Harbor Kings LB's Leg and Return</h3><div class="src">sportsdesk.example</div>
    <p>Bayview Harbor Kings linebacker Darrel Okonte suffered a scary injury in the League Championship Game against the Northport Gulls</p>
    <div class="actions"><span class="share"><svg width="9" height="8"><path d="M1 7 Q2 3 6 3 V1 L9 4 L6 7 V5 Q3 5 1 7Z" fill="#fff"/></svg>SHARE STORY▾</span><span class="vote">Vote Now (0)</span></div></article>
  <article class="card"><div class="thumb" role="img" aria-label="Dark futuristic city scene" style="background:linear-gradient(#6b6a64,#2c2c2e)"></div>
    <h3>Darrel Okonte Injury: Updates on Harbor Kings LB's Leg and Return</h3><div class="src">sportsdesk.example</div>
    <p>Bayview Harbor Kings linebacker Darrel Okonte suffered a scary injury in the League Championship Game against the Northport Gulls</p>
    <div class="actions"><span class="share"><svg width="9" height="8"><path d="M1 7 Q2 3 6 3 V1 L9 4 L6 7 V5 Q3 5 1 7Z" fill="#fff"/></svg>SHARE STORY▾</span><span class="vote">Vote Now (0)</span></div></article>
  <article class="card"><div class="thumb" role="img" aria-label="Hockey players and referees arguing" style="background:linear-gradient(135deg,#3c4f77,#1e2a44 50%,#d5d5d5)"></div>
    <h3>Darrel Okonte Injury: Updates on Harbor Kings LB's Leg and Return</h3><div class="src">sportsdesk.example</div>
    <p>Bayview Harbor Kings linebacker Darrel Okonte suffered a scary injury in the League Championship Game against the Northport Gulls</p>
    <div class="actions"><span class="share"><svg width="9" height="8"><path d="M1 7 Q2 3 6 3 V1 L9 4 L6 7 V5 Q3 5 1 7Z" fill="#fff"/></svg>SHARE STORY▾</span><span class="vote">Vote Now (0)</span></div></article>
  <article class="card"><div class="thumb" role="img" aria-label="Two football players talking after a game" style="background:linear-gradient(135deg,#1d2a3a,#6a7a5a 45%,#e4e4e4 70%,#b2432c)"></div>
    <h3>Darrel Okonte Injury: Updates on Harbor Kings LB's Leg and Return</h3><div class="src">sportsdesk.example</div>
    <p>Bayview Harbor Kings linebacker Darrel Okonte suffered a scary injury in the League Championship Game against the Northport Gulls</p>
    <div class="actions"><span class="share"><svg width="9" height="8"><path d="M1 7 Q2 3 6 3 V1 L9 4 L6 7 V5 Q3 5 1 7Z" fill="#fff"/></svg>SHARE STORY▾</span><span class="vote">Vote Now (0)</span></div></article>
  <article class="card"><div class="thumb" role="img" aria-label="Person on a rooftop ledge above a highway" style="background:linear-gradient(#9fb0c2,#6f7d5e 50%,#8c8a84)"></div>
    <h3>Darrel Okonte Injury: Updates on Harbor Kings LB's Leg and Return</h3><div class="src">sportsdesk.example</div>
    <p>Bayview Harbor Kings linebacker Darrel Okonte suffered a scary injury in the League Championship Game against the Northport Gulls</p>
    <div class="actions"><span class="share"><svg width="9" height="8"><path d="M1 7 Q2 3 6 3 V1 L9 4 L6 7 V5 Q3 5 1 7Z" fill="#fff"/></svg>SHARE STORY▾</span><span class="vote">Vote Now (0)</span></div></article>
  <article class="card"><div class="thumb" role="img" aria-label="Television studio set inside a stadium" style="background:linear-gradient(#c9ccd2,#b23a3a 50%,#2d4d33)"></div>
    <h3>Darrel Okonte Injury: Updates on Harbor Kings LB's Leg and Return</h3><div class="src">sportsdesk.example</div>
    <p>Bayview Harbor Kings linebacker Darrel Okonte suffered a scary injury in the League Championship Game against the Northport Gulls</p>
    <div class="actions"><span class="share"><svg width="9" height="8"><path d="M1 7 Q2 3 6 3 V1 L9 4 L6 7 V5 Q3 5 1 7Z" fill="#fff"/></svg>SHARE STORY▾</span><span class="vote">Vote Now (0)</span></div></article>
</div>
<footer class="footer">
  <div class="links">Home | About &nbsp;| &nbsp;Contact &nbsp;| &nbsp;FAQ</div>
  <div class="copy">© 2014 | Velnu, All Rights Reserved</div>
</footer>
</body>
</html>
```